Copper lark buildworks

Copper lark buildworks is a small construction company.
Who is a licenced builder, Carpenter, joiner,
working on heritage ,new build, speacial projects and sometimes furniture

Industry/Entity Type

Construction

```html
<!DOCTYPE html>
<html lang="en">
<head>
<meta charset="utf-8">
<title>Copper lark buildworks – Business Card</title>
<link rel="stylesheet" href="https://fonts.googleapis.com/css2?family=Montserrat:wght@500&family=Tinos:ital,wght@1,700&family=Noto+Serif:wght@400&family=Roboto+Condensed:wght@300&family=Arimo&display=swap">
<style>
  :root {
    --card-bg: #ffffff;
    --charcoal: #363435;
    --leaf: #8db03e;
    --ink: #2b2b2b;
    --white: #ffffff;
  }
  * { margin: 0; padding: 0; box-sizing: border-box; }
  html, body {
    width: 1200px; height: 735px; overflow: hidden;
    background: var(--card-bg);
  }
  .card { position: relative; width: 1200px; height: 735px; background: var(--card-bg); }

  .top-band {
    position: absolute; left: 69px; top: 64px; width: 1050px; height: 38px;
    background: var(--charcoal); border-radius: 22px 22px 0 0;
  }

  .brand {
    position: absolute; left: 130px; top: 190px; width: 460px;
    display: flex; flex-direction: column; align-items: center;
  }
  .brand-mark {
    width: 78px; height: 78px; border: 7px solid var(--leaf); margin-bottom: 22px;
  }
  .brand-name {
    font-family: "Montserrat", sans-serif; font-weight: 500;
    color: var(--leaf); font-size: 36px; letter-spacing: 5px;
    text-align: center; line-height: 1.15; text-transform: uppercase;
  }

  .divider {
    position: absolute; left: 624px; top: 155px; width: 2px; height: 233px;
    background: var(--charcoal);
  }

  .contact-name {
    position: absolute; left: 712px; top: 160px;
    font-family: "Tinos", serif; font-style: italic; font-weight: 700;
    font-size: 46px; color: var(--leaf);
  }
  .contact-phone {
    position: absolute; left: 787px; top: 231px;
    display: flex; align-items: center; gap: 12px;
    font-family: "Arimo", sans-serif; font-size: 30px; color: var(--ink);
  }
  .contact-phone svg { width: 28px; height: 28px; }

  .services {
    position: absolute; left: 69px; top: 458px; width: 1050px;
    text-align: center; font-family: "Noto Serif", serif;
    font-size: 27px; line-height: 37px; color: var(--ink);
  }

  .footer-band {
    position: absolute; left: 69px; top: 561px; width: 1050px; height: 102px;
    background: var(--leaf); border-radius: 0 0 22px 22px;
    display: flex; align-items: center; justify-content: center; gap: 30px;
    font-family: "Roboto Condensed", sans-serif; font-weight: 300;
    font-size: 36px; color: var(--white);
  }
  .footer-sep { font-size: 32px; }
  .social-square { width: 34px; height: 34px; background: var(--white); border-radius: 3px; }
  .social-circle { width: 36px; height: 36px; background: var(--white); border-radius: 50%; }
</style>
</head>
<body>
<div class="card">
  <div class="top-band"></div>

  <div class="brand">
    <div class="brand-mark"></div>
    <div class="brand-name">Copper lark<br>buildworks</div>
  </div>

  <div class="divider"></div>

  <div class="contact-name">Marcus Hale</div>
  <div class="contact-phone">
    <svg viewBox="0 0 28 28" aria-hidden="true">
      <circle cx="14" cy="14" r="14" fill="#111"/>
      <path d="M9.5 7.5c.6-.4 1.3-.3 1.7.3l1.3 2c.3.5.2 1.1-.2 1.5l-.9.8c.7 1.6 2 2.9 3.6 3.7l.8-.9c.4-.4 1-.5 1.5-.2l2 1.3c.6.4.7 1.1.3 1.7l-.7 1c-.6.8-1.6 1.1-2.5.8-4-1.4-7-4.4-8.4-8.4-.3-.9 0-1.9.8-2.5z" fill="#fff"/>
    </svg>
    <span>0412555018</span>
  </div>

  <p class="services">licenced builder, Carpenter, joiner, working on heritage ,new build,<br>special projects and sometimes furniture</p>

  <div class="footer-band">
    <span>www.copperlarkbuild.com</span>
    <span class="footer-sep">|</span>
    <span>E: info@copperlarkbuild.com</span>
    <span class="footer-sep">|</span>
    <span class="social-square" aria-label="Social profile"></span>
    <span class="footer-sep">|</span>
    <span class="social-circle" aria-label="Social profile"></span>
  </div>
</div>
</body>
</html>
```